Design Labels and Brand Look For Mens Soap Company

We are developing a mens soap line for a natural body wash and exfoliating bar. We will be selling this with our line of mens toiletry bags that we sell under the name of Corvane Totes on Quillmart. We are looking for you to design the product brand look with brand color palette and fonts.

The title for the mens body was is "Body Wash For Men". The title for the soap bar is "Exfoliating Bar Soap For Men"

We are providing the templates for these 2 items in PDF form. The final version of the design needs to be in a layered PSD format. You also need to send us the fonts used.

This soap will be sold on Quillmart. Do a search for "men's body wash" and "mens soap bar" you will see our competition on page one. We need to stand out with colors and design differentiaon.

Target Market(s)

Men

Industry/Entity Type

Skin Care Product

Requirements
Must have
• Layered PSD file with all fonts

```html
<!DOCTYPE html>
<html lang="en">
<head>
<meta charset="utf-8">
<title>Corvane Exfoliating Bar Soap – Wrap Label</title>
<link rel="stylesheet" href="https://fonts.googleapis.com/css2?family=EB+Garamond:wght@400;500&display=swap">
<style>
  :root {
    --paper: #ffffff;
    --navy: #150a55;
    --gold: #d4902c;
    --ink-light: #ffffff;
    --trim: #d6339a;
    --bleed: #29a8df;
  }
  html, body {
    margin: 0;
    padding: 0;
    width: 972px;
    height: 1200px;
    overflow: hidden;
    background: var(--paper);
  }
  .sheet {
    position: relative;
    width: 972px;
    height: 1200px;
    font-family: "EB Garamond", Georgia, serif;
  }
  .bleed-line {
    position: absolute;
    left: 29px; top: 33px;
    width: 914px; height: 1142px;
    border: 1px solid var(--bleed);
    box-sizing: border-box;
  }
  .trim-outer {
    position: absolute;
    left: 64px; top: 68px;
    width: 844px; height: 1072px;
    border: 1px solid var(--trim);
    box-sizing: border-box;
  }
  .wrap-band {
    position: absolute;
    left: 283px; top: 68px;
    width: 406px; height: 1010px;
    background: var(--navy);
  }
  .trim-wrap {
    position: absolute;
    left: 236px; top: 68px;
    width: 501px; height: 1010px;
    border: 1px solid var(--trim);
    box-sizing: border-box;
  }
  .fold {
    position: absolute;
    left: 236px;
    width: 501px;
    height: 0;
    border-top: 1px solid var(--trim);
  }
  .title {
    position: absolute;
    margin: 0;
    color: var(--ink-light);
    font-weight: 400;
    line-height: 1.05;
    letter-spacing: 0.01em;
    white-space: nowrap;
  }
  .title .for-men { color: var(--gold); display: block; }
  .title .line { display: block; }
  .brand-name {
    position: absolute;
    color: var(--gold);
    font-weight: 500;
    white-space: nowrap;
    text-align: center;
    line-height: 1;
  }
  .flipped { transform: rotate(180deg); }

  /* Top flap */
  .flap-top .title { left: 341px; top: 126px; width: 143px; font-size: 19px; text-align: left; }
  .flap-top .brand-name { left: 505px; top: 146px; width: 120px; font-size: 24px; }

  /* Back panel */
  .back .title { left: 336px; top: 274px; width: 300px; font-size: 19.5px; text-align: center; }
  .back .brand-name { left: 428px; top: 371px; width: 120px; font-size: 21px; }

  /* Front face */
  .front .brand-name { left: 393px; top: 522px; width: 180px; font-size: 32px; }
  .front .title { left: 286px; top: 596px; width: 400px; font-size: 29px; text-align: center; }

  /* Lower panel */
  .lower .brand-name { left: 347px; top: 826px; width: 120px; font-size: 25px; }
  .lower .title { left: 487px; top: 810px; font-size: 19px; text-align: left; }

  /* Bottom flap */
  .flap-bottom .title { left: 341px; top: 972px; width: 143px; font-size: 19px; text-align: left; }
  .flap-bottom .brand-name { left: 505px; top: 990px; width: 120px; font-size: 24px; }
</style>
</head>
<body>
<main class="sheet">
  <div class="bleed-line"></div>
  <div class="trim-outer"></div>
  <div class="wrap-band"></div>
  <div class="trim-wrap"></div>
  <div class="fold" style="top:253px"></div>
  <div class="fold" style="top:437px"></div>
  <div class="fold" style="top:744px"></div>
  <div class="fold" style="top:929px"></div>

  <section class="panel flap-top">
    <div class="brand-name flipped">Corvane</div>
    <h2 class="title flipped"><span class="line">EXFOLIATING</span><span class="line">BAR SOAP</span><span class="for-men">FOR MEN</span></h2>
  </section>

  <section class="panel back">
    <h2 class="title flipped"><span class="line">EXFOLIATING</span><span class="line">BAR SOAP</span><span class="for-men">FOR MEN</span></h2>
    <div class="brand-name flipped">Corvane</div>
  </section>

  <section class="panel front">
    <div class="brand-name">Corvane</div>
    <h1 class="title"><span class="line">EXFOLIATING</span><span class="line">BAR SOAP</span><span class="for-men">FOR MEN</span></h1>
  </section>

  <section class="panel lower">
    <div class="brand-name">Corvane</div>
    <h2 class="title"><span class="line">EXFOLIATING</span><span class="line">BAR SOAP</span><span class="for-men">FOR MEN</span></h2>
  </section>

  <section class="panel flap-bottom">
    <div class="brand-name flipped">Corvane</div>
    <h2 class="title flipped"><span class="line">EXFOLIATING</span><span class="line">BAR SOAP</span><span class="for-men">FOR MEN</span></h2>
  </section>
</main>
</body>
</html>
```